Amenity Menu @ Hotel Larkspur

Create an Amenity Menu for our rooms. Should match a modern, clean, concise style with easy readability for all ages.

I've included a working menu with all the copy - not happy with this version created at our local copy store. Readability is not great, sections are not clearly delineated. Would like the SPA Services to stand out from the rest of the menu. The top two sections do not bring revenue (convenience items), but the bottom two do bring revenue, so clients should be drawn to those areas.

www.hotellarkspur.ca (our website) - will give a sense of our style and look we're going for. Stock images of massage or cool icons to go along with categories? maybe?.

```html
<!DOCTYPE html>
<html lang="en">
<head>
<meta charset="utf-8">
<title>Amenity Menu · Hotel Larkspur</title>
<link href="https://fonts.googleapis.com/css2?family=Montserrat:ital,wght@0,700;0,800;1,700&family=Open+Sans:ital,wght@1,400;1,600;1,700&display=swap" rel="stylesheet">
<style>
  :root {
    --bg-deep: #141216;
    --bg-mid: #2a2730;
    --ink: #ffffff;
    --ink-soft: #d9d6de;
    --ink-muted: #b9b4c2;
    --accent: #7b2fa6;
    --accent-bright: #8e3cc0;
    --band-start: #5a1f80;
  }
  * { box-sizing: border-box; margin: 0; padding: 0; }
  html, body { width: 973px; height: 1200px; overflow: hidden; background: var(--bg-deep); }
  .menu {
    position: relative; width: 973px; height: 1200px; overflow: hidden;
    color: var(--ink); font-family: "Open Sans", Arial, sans-serif; font-style: italic;
  }
  .menu__backdrop {
    position: absolute; inset: 0;
    background: radial-gradient(ellipse at 50% 45%, var(--bg-mid) 0%, #1d1b21 55%, var(--bg-deep) 100%);
  }
  .block { position: absolute; }

  .title { top: 46px; left: 0; width: 100%; text-align: center; }
  .title__main {
    font-family: "Montserrat", Arial, sans-serif; font-weight: 800; font-style: normal;
    font-size: 46px; letter-spacing: -0.5px; line-height: 1;
  }
  .title__main .accent { color: var(--accent); }
  .title__sub { font-size: 20px; letter-spacing: 1px; margin-top: 8px; }

  .heading {
    font-family: "Montserrat", Arial, sans-serif; font-weight: 700; font-style: italic;
    font-size: 20px; text-transform: uppercase; letter-spacing: 0.3px; line-height: 1;
  }
  .band {
    position: absolute; height: 34px; padding-left: 12px;
    display: flex; align-items: center;
    background: linear-gradient(90deg, var(--band-start) 0%, rgba(90,31,128,0.55) 55%, rgba(90,31,128,0.15) 100%);
  }
  .list { list-style: none; font-size: 15.5px; line-height: 22.7px; text-transform: uppercase; color: var(--ink-soft); }
  .priced li { display: flex; justify-content: space-between; }
  .priced .price { font-weight: 700; font-style: italic; color: var(--ink); }

  .complimentary { top: 163px; left: 53px; }
  .complimentary .list { margin-top: 14px; }

  .borrow { top: 163px; left: 545px; width: 380px; }
  .borrow .avail { position: absolute; right: 0; top: 23px; font-size: 12px; color: var(--ink-muted); }
  .borrow .list { margin-top: 14px; }
  .borrow .notice { margin-top: 12px; font-size: 13px; line-height: 19px; color: var(--ink-muted); width: 375px; }

  .impress-band { top: 349px; left: 51px; width: 482px; }
  .impress { top: 389px; left: 53px; width: 446px; }
  .impress .package { margin-top: 6px; font-size: 15.5px; color: var(--ink-soft); }

  .spa-band { top: 536px; left: 51px; width: 866px; }
  .spa-intro { top: 574px; left: 57px; font-size: 18px; font-variant: small-caps; letter-spacing: 0.6px; }
  .spa-col { top: 612px; }
  .spa-col__title {
    height: 50px; display: flex; flex-direction: column; justify-content: flex-end; text-align: center;
    font-weight: 700; font-size: 18px; font-variant: small-caps; text-decoration: underline; line-height: 1.25;
  }
  .rates { margin-top: 14px; font-size: 16px; line-height: 23px; }
  .rates li { display: grid; list-style: none; }
  .rates .price { font-weight: 700; }
  .spa-col--aroma { left: 53px; width: 248px; }
  .spa-col--aroma .rates { padding-left: 46px; }
  .spa-col--aroma li { grid-template-columns: 112px auto; }
  .spa-col--rmt { left: 347px; width: 318px; }
  .spa-col--rmt .rates { padding-left: 68px; }
  .spa-col--rmt li { grid-template-columns: 115px auto; }
  .spa-col--stone { left: 711px; width: 200px; }
  .spa-col--stone .rates { padding-left: 32px; margin-top: 24px; }
  .spa-col--stone li { grid-template-columns: 74px auto; }
  .spa-col--stone .tag { font-weight: 400; }

  .upgrade-band { top: 771px; left: 51px; width: 858px; }
  .upgrade-left { top: 814px; left: 53px; width: 378px; }
  .upgrade-right { top: 814px; left: 545px; width: 352px; }

  .footnote { top: 1121px; left: 53px; font-size: 15px; color: var(--ink-soft); }
  .brand {
    top: 1098px; left: 612px; display: flex; align-items: center; gap: 12px;
    font-family: "Montserrat", Arial, sans-serif; font-style: normal; font-weight: 700;
    font-size: 24px; letter-spacing: 2px; color: var(--ink);
  }
  .brand__dot { width: 14px; height: 14px; border-radius: 50%; background: var(--accent-bright); }
</style>
</head>
<body>
<main class="menu">
  <div class="menu__backdrop" role="img" aria-label="Dark charcoal damask swirl pattern background"></div>

  <header class="block title">
    <h1 class="title__main"><span class="accent">AMENITY</span> MENU</h1>
    <p class="title__sub">FORGOT SOMETHING? WE CAN HELP!</p>
  </header>

  <section class="block complimentary">
    <h2 class="heading">Complimentary - Just Ask</h2>
    <ul class="list">
      <li>Laundry bags</li>
      <li>Toothbrush and toothpaste</li>
      <li>Vanity kit (nail file, Q-tips, makeup pads)</li>
      <li>Razor</li>
      <li>Ear plugs</li>
      <li>Sewing kit</li>
    </ul>
  </section>

  <section class="block borrow">
    <h2 class="heading">Borrow During Your Stay</h2>
    <span class="avail">Based on availability</span>
    <ul class="list">
      <li>Fan</li>
      <li>Curling iron</li>
      <li>Hairdryer</li>
      <li>Extra pillows</li>
      <li>Select computer cords/ mobile chargers</li>
      <li>Umbrella</li>
      <li>Board games</li>
      <li>DVD's/DVD player</li>
    </ul>
    <p class="notice">Kindly note that upon borrowing there will be a deposit charged to your folio - if items borrowed are not returned or left in your room upon departure you will be charged for the full price of the item.<br>We appreciate your understanding.</p>
  </section>

  <div class="band impress-band"><h2 class="heading">Impress Someone</h2></div>
  <section class="block impress">
    <ul class="list priced">
      <li><span>Truffles or chocolate covered strawberries</span><span class="price">18</span></li>
      <li><span>Bottle of wine (red or white)</span><span class="price">24</span></li>
      <li><span>Rose petal arrangement</span><span class="price">24</span></li>
      <li><span>A dozen long stem roses</span><span class="price">35</span></li>
    </ul>
    <p class="package">*Create a full package with all the above for $99</p>
  </section>

  <div class="band spa-band"><h2 class="heading">Exclusive Spa Services</h2></div>
  <p class="block spa-intro">Book a treatment in our “Skylight Loft” oasis, or the comfort of your own room.</p>

  <section class="block spa-col spa-col--aroma">
    <h3 class="spa-col__title"><span>Deep Tissue</span><span>Aromatherapy Massage</span></h3>
    <ul class="rates">
      <li><span>30 min.</span><span class="price">$85</span></li>
      <li><span>1 hr.</span><span class="price">$115</span></li>
      <li><span>1.5 hrs.</span><span class="price">$165</span></li>
      <li><span>2 hrs.</span><span class="price">$225</span></li>
    </ul>
  </section>

  <section class="block spa-col spa-col--rmt">
    <h3 class="spa-col__title"><span>Registered Massage Therapists</span></h3>
    <ul class="rates">
      <li><span>1 hr.</span><span class="price">$120</span></li>
      <li><span>1.5 hrs.</span><span class="price">$175</span></li>
      <li><span>2 hrs.</span><span class="price">$240</span></li>
    </ul>
  </section>

  <section class="block spa-col spa-col--stone">
    <h3 class="spa-col__title"><span>Hot Stone Massage</span></h3>
    <ul class="rates">
      <li><span>1.5 hr.</span><span class="price">$185</span></li>
      <li><span>1.5 hr.</span><span class="price">$195 <span class="tag">(RMT)</span></span></li>
    </ul>
  </section>

  <div class="band upgrade-band"><h2 class="heading">Upgraded Amenities</h2></div>
  <section class="block upgrade-left">
    <ul class="list priced">
      <li><span>Branded toothbrush</span><span class="price">4</span></li>
      <li><span>Dental floss</span><span class="price">4</span></li>
      <li><span>Mouth wash</span><span class="price">4</span></li>
      <li><span>Toothpaste (travel size)</span><span class="price">3</span></li>
      <li><span>Branded razor</span><span class="price">12</span></li>
      <li><span>Handwash detergant</span><span class="price">4</span></li>
      <li><span>Shaving cream (travel size)</span><span class="price">4</span></li>
      <li><span>Manicure set (with tweezers)</span><span class="price">15</span></li>
      <li><span>Hair spray (travel size)</span><span class="price">6</span></li>
      <li><span>Bobby pins</span><span class="price">4</span></li>
      <li><span>Deoderant</span><span class="price">5</span></li>
      <li><span>Loofah</span><span class="price">3</span></li>
    </ul>
  </section>
  <section class="block upgrade-right">
    <ul class="list priced">
      <li><span>Contact lens solution</span><span class="price">8</span></li>
      <li><span>Feminine hygiene products</span><span class="price">5</span></li>
      <li><span>Safety pins</span><span class="price">3</span></li>
      <li><span>Lip butter</span><span class="price">6</span></li>
      <li><span>Lint roller</span><span class="price">6</span></li>
      <li><span>HL Hoot: wise “plush” owl</span><span class="price">24</span></li>
    </ul>
  </section>

  <p class="block footnote">*All prices are plus taxes</p>

  <div class="block brand" aria-label="Hotel Larkspur">
    <span class="brand__dot"></span>
    <span>Hotel Larkspur</span>
  </div>
</main>
</body>
</html>
```